Embers Beneath Silver Lanterns

An image of dancing couple under spotlight. The lady with red dress and the man with black suit.

Use, 1400x1400 pixels
JPG File type
72-300 dpi
RGB color Scheme (Not CMYK)

Target Market(s)

Adults 25 and over who could be interested in ballroom dances or like to hear Argentinian tango or Viennese Waltze. The design should transfer a passionate filling to the viewer. The design must carry a dance "figure"that can present both tango, and waltz dance.

Font styles to use
Decorative

Colors

Designer to choose colors to be used in the design.

```html
<!DOCTYPE html>
<html lang="en">
<head>
<meta charset="utf-8">
<title>Embers Beneath Silver Lanterns</title>
<link href="https://fonts.googleapis.com/css2?family=Great+Vibes&display=swap" rel="stylesheet">
<style>
  :root {
    --backdrop: #efece6;
    --sleeve-white: #ffffff;
    --dress-red: #b3120f;
    --dress-deep: #5e0806;
    --suit-black: #141212;
    --skin-warm: #8a5a3c;
    --gold-light: #fff3c4;
    --gold-mid: #f0a12a;
    --gold-deep: #9c4a06;
    --ink-outline: #1a0f08;
    --hub-grey: #d6d3cc;
    --hub-line: #6f6a62;
  }
  * { margin: 0; padding: 0; box-sizing: border-box; }
  html, body { width: 1200px; height: 730px; overflow: hidden; }
  body { background: var(--backdrop); position: relative; font-family: "Great Vibes", cursive; }

  .album-cover {
    position: absolute; left: 177px; top: 135px; width: 510px; height: 486px;
    background: var(--sleeve-white); overflow: hidden;
    box-shadow: 0 2px 6px rgba(0,0,0,.25);
  }
  .dancers-photo {
    position: absolute; left: 0; top: 0; width: 430px; height: 100%;
    background:
      radial-gradient(ellipse 34% 50% at 30% 45%, var(--dress-red), transparent 75%),
      radial-gradient(ellipse 40% 30% at 62% 40%, var(--skin-warm), transparent 70%),
      linear-gradient(100deg, var(--dress-deep) 0%, var(--dress-red) 30%, var(--suit-black) 55%, var(--suit-black) 80%, rgba(20,18,18,0) 100%);
  }
  .title {
    position: absolute; line-height: 1; white-space: nowrap;
    background: linear-gradient(180deg, var(--gold-light) 0%, var(--gold-mid) 50%, var(--gold-deep) 100%);
    -webkit-background-clip: text; background-clip: text; color: transparent;
    -webkit-text-stroke: 1.5px var(--ink-outline);
    filter: drop-shadow(2px 2px 0 #fff) drop-shadow(3px 3px 1px rgba(0,0,0,.7));
  }
  .album-cover .title-kicker { left: 26px; top: 150px; font-size: 52px; }
  .album-cover .title-main { left: 70px; top: 218px; font-size: 112px; }
  .album-cover .title-sub { left: 104px; top: 336px; font-size: 100px; }

  .disc {
    position: absolute; left: 672px; top: 159px; width: 428px; height: 428px;
    border-radius: 50%; background: var(--sleeve-white); overflow: hidden;
    box-shadow: 0 2px 6px rgba(0,0,0,.25);
  }
  .disc .dancers-photo { width: 320px; }
  .disc .title-kicker { left: 92px; top: 58px; font-size: 50px; }
  .disc .title-main { left: 44px; top: 268px; font-size: 66px; }
  .disc .title-sub { left: 92px; top: 326px; font-size: 58px; }
  .disc-hub { position: absolute; left: 0; top: 0; }
</style>
</head>
<body>
  <section class="album-cover">
    <div class="dancers-photo" role="img" aria-label="Photograph of a tango couple: lady in a red satin dress with her leg raised, man in a black suit"></div>
    <h1 class="title title-kicker">Embers Beneath</h1>
    <p class="title title-main">Silver</p>
    <p class="title title-sub">Lanterns</p>
  </section>

  <section class="disc">
    <div class="dancers-photo" role="img" aria-label="Photograph of the same tango couple in red dress and black suit"></div>
    <p class="title title-kicker">Embers Beneath</p>
    <p class="title title-main">Silver</p>
    <p class="title title-sub">Lanterns</p>
    <svg class="disc-hub" width="428" height="428" viewBox="0 0 428 428" aria-hidden="true">
      <circle cx="214" cy="214" r="72" fill="var(--hub-grey)" fill-opacity=".85" stroke="var(--hub-line)" stroke-width="1.5"/>
      <circle cx="214" cy="214" r="56" fill="none" stroke="var(--hub-line)" stroke-width="1"/>
      <circle cx="214" cy="214" r="20" fill="var(--backdrop)" stroke="var(--hub-line)" stroke-width="1"/>
    </svg>
  </section>
</body>
</html>
```